Chiropractor wanting creative graphic depicting power for pull up bannerstand

Harbour Crest in New Zealand. We require a graphic for a pull up bannerstand for shopping mall promotions where we do chiropractic postural evaluations. We don't want to use the word chiropractic, and don't want pictures of spines, or lists of symptoms.
We want to express the nerve system dysfunction associated with poor spinal alignment as a power problem (like electricity). Our philosophy is the brain being like a battery, with the power flowing over the nerve system. Full power gives great health, great function, great performance, therefore this is of benefit to all people. Our target market is relatively healthy people who want to be better/extraordinary.
For extraordinary health you need the power of the nerve system turned on. Needs to be put in a positive light of what people have to gain.
We are looking for simplicity, funky, creative, eye-catching, and stops the passer by.

Reason: Everyone on the wrong track...need to read brief closely

Please read previous brief closely. Please do not use the word chiropractic...not even saying Harbour Crest. Please do not have pictures of spines. No pictures of symptoms like back pain. Please don't just drop our business card into banner. We are looking for something that makes people stop to look. Has to be to do with electrical power, as we view the nervous system like electrical power. 

I hope that this clarifies the job.

Target Market(s)

Relatively healthy people who want to be better/extraordinary. 25-50 yr old, more female than male

Industry/Entity Type

Shopping

Requirements
Must have
• Must have website address www.harbourcrestchiro.co.nz and our logo (though we don't want these to dominate)
Should not have
• Anything relating to symptoms

```html
<!DOCTYPE html>
<html lang="en">
<head>
<meta charset="utf-8">
<title>Harbour Crest – Pull-up Banner</title>
<link rel="stylesheet" href="https://fonts.googleapis.com/css2?family=Questrial&family=Kalam:wght@300&family=Tinos:wght@700&family=Righteous&display=swap">
<style>
  :root {
    --page: #ffffff;
    --green-deep: #0a9440;
    --green-mid: #3fae3a;
    --green-light: #6cbf31;
    --lime: #b6c921;
    --lime-soft: #d9e46a;
    --white: #ffffff;
    --ink: #1b1b1b;
    --photo-dark: #05070b;
    --photo-glow: #5e86b5;
  }
  * { margin: 0; padding: 0; box-sizing: border-box; }
  html, body {
    width: 1200px;
    height: 2465px;
    overflow: hidden;
    background: var(--page);
  }
  .canvas {
    position: relative;
    width: 1200px;
    height: 2465px;
    background: var(--page);
  }
  .banner {
    position: absolute;
    left: 106px;
    top: 71px;
    width: 968px;
    height: 2280px;
    background: radial-gradient(ellipse 70% 55% at 50% 45%, var(--green-light) 0%, var(--green-mid) 55%, var(--green-deep) 100%);
  }
  .brand-panel {
    position: absolute;
    left: 81px;
    top: 67px;
    width: 806px;
    height: 490px;
    background: var(--lime);
    box-shadow: 0 6px 14px rgba(0, 0, 0, 0.35);
  }
  .brand-name {
    position: absolute;
    left: 30px;
    top: 330px;
    font-family: "Questrial", sans-serif;
    font-size: 84px;
    line-height: 84px;
    color: var(--white);
    letter-spacing: -0.5px;
    white-space: nowrap;
  }
  .brand-tagline {
    position: absolute;
    left: 197px;
    top: 430px;
    font-family: "Kalam", cursive;
    font-weight: 300;
    font-size: 34px;
    line-height: 40px;
    color: var(--lime-soft);
    letter-spacing: 1px;
    white-space: nowrap;
  }
  .message {
    position: absolute;
    left: 81px;
    width: 806px;
    font-family: "Tinos", serif;
    font-weight: 700;
    color: var(--white);
    font-size: 36px;
    line-height: 44px;
  }
  .message--intro {
    top: 626px;
    text-align: justify;
  }
  .message--closing {
    top: 1832px;
    text-align: center;
  }
  .hero-visual {
    position: absolute;
    left: 173px;
    top: 977px;
    width: 621px;
    height: 828px;
    background: radial-gradient(ellipse 55% 50% at 55% 40%, var(--photo-glow) 0%, #1d2e47 45%, var(--photo-dark) 80%);
  }
  .web-panel {
    position: absolute;
    left: 74px;
    top: 2024px;
    width: 806px;
    height: 180px;
    background: var(--lime);
    box-shadow: 0 6px 14px rgba(0, 0, 0, 0.35);
    display: flex;
    align-items: center;
    justify-content: center;
  }
  .web-address {
    font-family: "Righteous", sans-serif;
    font-size: 40px;
    color: var(--ink);
    text-transform: uppercase;
    letter-spacing: 0.5px;
    white-space: nowrap;
  }
</style>
</head>
<body>
<div class="canvas">
  <main class="banner">
    <header class="brand-panel">
      <p class="brand-name">harbour crest</p>
      <p class="brand-tagline">your family wellness team</p>
    </header>

    <p class="message message--intro">Your brain is a battery, and your nerve system is the wiring that carries its power to every part of you. When that power flows freely you feel it: more energy, sharper focus, deeper sleep and stronger performance in everything you do. Switch on your full power and go from feeling good to feeling truly extraordinary.</p>

    <div class="hero-visual" role="img" aria-label="Glowing blue anatomical head in profile with a charged battery inside the brain, on a black background"></div>

    <p class="message message--closing">Are you running on full power today?<br>Ask us about a posture check while you shop<br>and find out how much more you have to gain.</p>

    <footer class="web-panel">
      <p class="web-address">www.harbourcrestchiro.co.nz</p>
    </footer>
  </main>
</div>
</body>
</html>
```